kf novum
My service company has specialists in Sales, Marketing and Change Management. Our target group is the 1st and 2nd management level of enterprises, who want to align their strategy at new market situations or to change their distribution, communication or product concept.
We help our clients in defined time frames or projects not only in defining new strategies and concepts but also in implementation and measurements of the results.
I'm looking for a design of business cards and A4 letter paper. The company name is "kf novum"; my name ist Konrad Fels...
So the name of my company stands for Management on time (kf novum) and kf stands for my name (initials)
Logo see enclosed.

```html
<!DOCTYPE html>
<html lang="de">
<head>
<meta charset="utf-8">
<title>kf novum – Briefbogen</title>
<link href="https://fonts.googleapis.com/css2?family=Michroma&display=swap" rel="stylesheet">
<style>
  :root {
    --backdrop: #75777a;
    --paper: #ffffff;
    --navy: #1f2631;
    --ink: #3a3d42;
    --mark: #2b2f36;
  }
  * { margin: 0; padding: 0; box-sizing: border-box; }
  html, body { width: 900px; height: 1200px; overflow: hidden; background: var(--backdrop); }
  body { position: relative; font-family: "Michroma", "Arial", sans-serif; color: var(--ink); }

  .sheet {
    position: absolute; left: 56px; top: 43px;
    width: 776px; height: 1114px;
    background: var(--paper);
  }
  .edge-bar {
    position: absolute; left: 832px; width: 11px;
    background: var(--navy);
  }
  .edge-bar--top { top: 43px; height: 194px; }
  .edge-bar--bottom { top: 1008px; height: 149px; }

  .brand-name {
    position: absolute; right: 50px; top: 203px;
    font-size: 27px; letter-spacing: 0.5px;
    color: var(--mark); line-height: 1;
  }
  .sender-line {
    position: absolute; left: 93px; top: 186px;
    font-size: 6.4px; color: var(--ink); letter-spacing: 0.1px;
  }
  .fold-mark {
    position: absolute; left: 9px; width: 11px; height: 1px;
    background: var(--ink);
  }
  .fold-mark--1 { top: 393px; }
  .fold-mark--2 { top: 556px; }
  .fold-mark--3 { top: 786px; }

  .contact {
    position: absolute; left: 587px; top: 960px;
    font-size: 8.6px; line-height: 14.6px; color: var(--ink);
    letter-spacing: 0.6px;
  }
  .contact-group { position: relative; padding-left: 22px; margin-bottom: 5px; }
  .contact-row { position: relative; }
  .contact-company { color: var(--navy); font-weight: 700; letter-spacing: 0.9px; }
  .contact-icon {
    position: absolute; left: -22px; top: 2px;
    width: 10px; height: 10px; fill: var(--navy);
  }
</style>
</head>
<body>
  <div class="sheet">
    <div class="brand-name">kf novum</div>
    <p class="sender-line">kf novum · Beispielweg 7 · 54321 Beispielstadt</p>

    <span class="fold-mark fold-mark--1"></span>
    <span class="fold-mark fold-mark--2"></span>
    <span class="fold-mark fold-mark--3"></span>

    <address class="contact" style="font-style:normal">
      <div class="contact-group">
        <div class="contact-row">
          <svg class="contact-icon" viewBox="0 0 10 10" aria-hidden="true"><path d="M5 0C3 0 1.6 1.5 1.6 3.4 1.6 6 5 10 5 10s3.4-4 3.4-6.6C8.4 1.5 7 0 5 0zm0 4.8a1.4 1.4 0 110-2.8 1.4 1.4 0 010 2.8z"/></svg>
          <span class="contact-company">kf novum</span>
        </div>
        <div class="contact-row">Konrad Fels</div>
        <div class="contact-row">Beispielweg 7</div>
        <div class="contact-row">54321 Beispielstadt</div>
      </div>
      <div class="contact-group">
        <div class="contact-row">
          <svg class="contact-icon" viewBox="0 0 10 10" aria-hidden="true"><path d="M2.2 0.5L3.8 2.6 2.9 3.7C3.6 5.4 4.6 6.5 6.3 7.2L7.4 6.2 9.5 7.8 8.4 9.5C4.2 9.2 0.8 5.8 0.5 1.6z"/></svg>
          +49 2345 6789012
        </div>
        <div class="contact-row">
          <svg class="contact-icon" viewBox="0 0 10 10" aria-hidden="true"><path d="M2.5 0h5a1 1 0 011 1v8a1 1 0 01-1 1h-5a1 1 0 01-1-1V1a1 1 0 011-1zm.4 1.2v6.4h4.2V1.2zM5 8.2a.6.6 0 100 1.2.6.6 0 000-1.2z"/></svg>
          +49 172 7654321
        </div>
      </div>
      <div class="contact-group">
        <div class="contact-row">
          <svg class="contact-icon" viewBox="0 0 10 10" aria-hidden="true"><circle cx="5" cy="5" r="4.5" fill="none" stroke="#1f2631" stroke-width="1"/><path d="M0.5 5h9M5 0.5c-2.2 2.5-2.2 6.5 0 9M5 0.5c2.2 2.5 2.2 6.5 0 9" fill="none" stroke="#1f2631" stroke-width="0.8"/></svg>
          www.kfnovum.com
        </div>
        <div class="contact-row">
          <svg class="contact-icon" viewBox="0 0 10 10" aria-hidden="true"><path d="M0.5 2h9v6.5h-9zM1 2.5L5 5.8 9 2.5" fill="#1f2631" stroke="#fff" stroke-width="0.6"/></svg>
          info@kfnovum.com
        </div>
      </div>
    </address>
  </div>
  <div class="edge-bar edge-bar--top"></div>
  <div class="edge-bar edge-bar--bottom"></div>
</body>
</html>
```